New education centre needs a flyer design

We need a flyer design for this coming holiday program in science for students in primary school. Its a science program for 2 days in which experiments, applications will be conducted to teach a concept. I will attach what we will be doing but the description needs to be as brief as possible so that viewers who see it will be interested and call to find out more. I leave the design and colors to you but it has to be attractive and eye catching. Please see attach for information on details of the program as well as the logo of our education centre in Singapore.
Primary School Students and Parents
Education

```html
<!DOCTYPE html>
<html lang="en">
<head>
<meta charset="utf-8">
<title>Bright Spark Campus – Holiday Science Camp</title>
<link rel="stylesheet" href="https://fonts.googleapis.com/css2?family=Tinos:ital,wght@1,700&display=swap">
<style>
  :root {
    --navy: #1d3a6b;
    --magenta: #e0197d;
    --red: #cf1a1f;
    --green: #4fae2c;
    --gold: #d8b418;
    --ink: #151515;
    --paper: #ffffff;
    --stripe-navy: #1b2f5c;
    --stripe-pink: #d8307f;
    --stripe-yellow: #f2c81c;
    --stripe-green: #58a83a;
    --stripe-red: #d4262b;
  }
  * { margin: 0; padding: 0; box-sizing: border-box; }
  html, body { width: 1200px; height: 900px; overflow: hidden; background: var(--paper); }
  .flyer {
    position: relative; width: 1200px; height: 900px; overflow: hidden;
    background: var(--paper);
    font-family: "Tinos", "Times New Roman", serif;
    font-style: italic; font-weight: 700; color: var(--ink);
  }
  .stripe {
    position: absolute; left: 0; width: 1200px; height: 6px;
    background: repeating-linear-gradient(90deg,
      var(--stripe-navy) 0 112px, var(--stripe-pink) 112px 224px,
      var(--stripe-yellow) 224px 336px, var(--stripe-green) 336px 448px,
      var(--stripe-red) 448px 560px);
  }
  .stripe--top { top: 0; }
  .stripe--bottom { bottom: 0; }

  .lab-backdrop {
    position: absolute; left: 70px; top: 620px; width: 700px; height: 280px;
    background: linear-gradient(90deg, rgba(170,200,230,.35), rgba(240,200,160,.35) 45%, rgba(190,230,200,.35) 75%, rgba(250,210,220,.3));
    filter: blur(6px);
  }

  .brand {
    position: absolute; left: 20px; top: 120px; width: 270px;
    display: flex; align-items: center; gap: 12px;
    color: var(--navy); font-size: 30px; line-height: 1.1;
  }
  .brand__dot { width: 34px; height: 34px; border-radius: 50%; background: var(--navy); flex: none; }

  .headline { position: absolute; left: 325px; top: 28px; color: var(--navy); font-size: 25px; line-height: 46px; }
  .headline .own { color: var(--magenta); }
  .camp-line { position: absolute; left: 323px; top: 131px; color: var(--red); font-size: 26px; }
  .camp-line .holiday { color: var(--green); }

  .intro { position: absolute; left: 320px; top: 199px; width: 410px; font-size: 18px; line-height: 28px; }
  .invite { position: absolute; left: 40px; top: 377px; width: 690px; font-size: 18px; line-height: 27px; }

  .call { position: absolute; left: 38px; top: 488px; color: var(--magenta); font-size: 30px; }
  .call .phone { color: var(--red); font-size: 37px; }

  .hurry { position: absolute; left: 34px; top: 560px; color: var(--gold); font-size: 68px; display: flex; align-items: baseline; gap: 22px; }
  .hurry .slots { color: var(--magenta); font-size: 30px; }

  .contact { position: absolute; left: 34px; top: 720px; text-shadow: 1px 1px 2px rgba(0,0,0,.35); }
  .contact__title { font-size: 33px; margin-left: 6px; margin-bottom: 18px; }
  .contact__line { font-size: 22px; line-height: 33px; }

  .photo { position: absolute; }
  .photo--lesson { left: 760px; top: 172px; width: 411px; height: 260px; background: linear-gradient(135deg, #c9c2b6, #e8e2d8 45%, #b9c6cf); }
  .photo--pipette { left: 760px; top: 443px; width: 208px; height: 262px; background: linear-gradient(160deg, #4f5d6a, #9aa6ad 50%, #e6d9c8); }
  .photo--flasks { left: 977px; top: 443px; width: 194px; height: 262px; background: linear-gradient(160deg, #f1f1f1, #e9b6cf 55%, #9fd0c6); }
  .photo--magnifier { left: 760px; top: 720px; width: 411px; height: 152px; background: linear-gradient(90deg, #d8dce2, #f1ebe4 50%, #e7b7bd); }
</style>
</head>
<body>
<main class="flyer">
  <div class="stripe stripe--top"></div>
  <div class="lab-backdrop" role="img" aria-label="Faint laboratory glassware with coloured liquids"></div>

  <div class="brand">
    <span class="brand__dot"></span>
    <span class="brand__name">Bright Spark Campus</span>
  </div>

  <p class="headline">Home alone ? Ever thought of making your very <span class="own">OWN</span> burglar alarm<br>to feel safe and impress your family and friends?</p>
  <p class="camp-line">In our <span class="holiday">holiday camp</span>, this is exactly what we are going to be doing!!</p>

  <p class="intro">We are going to guide you to build unique items by discovering what electricity is all about in a fun and exciting way by touching base on lights, batteries, electrical circuits and more.</p>

  <p class="invite">Don’t wait any longer! Be prepared to let your creative juices flow and your imagination come alive by creating your very own personalized electrical items!</p>

  <p class="call">Call us at <span class="phone">61759024</span> to reserve your places now.</p>
  <p class="hurry">Hurry !!! <span class="slots">Limited slots available.</span></p>

  <address class="contact">
    <p class="contact__title">Address:</p>
    <p class="contact__line">118 Meadowbank Road</p>
    <p class="contact__line">Singapore 428190</p>
    <p class="contact__line">Email: hello@brightspark.sg</p>
  </address>

  <div class="photo photo--lesson" role="img" aria-label="Teacher guiding two students through an experiment"></div>
  <div class="photo photo--pipette" role="img" aria-label="Children in goggles working with test tubes"></div>
  <div class="photo photo--flasks" role="img" aria-label="Girl in goggles with colourful flasks"></div>
  <div class="photo photo--magnifier" role="img" aria-label="Two children looking through a magnifying glass"></div>

  <div class="stripe stripe--bottom"></div>
</main>
</body>
</html>
```